Powerpoint master slides for business

Hello everyone,

I am looking for a new PowerPoint master slide that should be modern, slim and yet suitable for business.

I have uploaded a few pictures, which should serve as A. orientation for my presentation. A logo should be placed on the right-hand side of the cover sheet and all subsequent slides - please insert a placeholder here. Also attached are our company colors, which must be taken into account.

Basically, I would find 6 to 10 slides (cover sheet, classic slide, end, etc.) good.

PS: The slides are intended for general everyday work, ie the design should be subtle and easily adaptable to different situations, but still look chic, modern and classy.

```html
<!DOCTYPE html>
<html lang="en">
<head>
<meta charset="utf-8">
<title>Veridane – Business Slide Master</title>
<link rel="stylesheet" href="https://fonts.googleapis.com/css2?family=Bebas+Neue&family=Montserrat:wght@400;500;600;700&display=swap">
<style>
  :root{
    --navy:#17174a;
    --green:#6cc04a;
    --deep:#12325a;
    --canvas:#d9d9d9;
    --white:#ffffff;
    --ink:#1d1d2b;
    --ghost:#e4e4ee;
    --ghost-green:#eef6ea;
  }
  *{margin:0;padding:0;box-sizing:border-box}
  html,body{width:772px;height:1200px;overflow:hidden;background:var(--canvas)}
  body{position:relative;font-family:"Montserrat",sans-serif;color:var(--ink)}
  .slide{position:absolute;width:286px;height:179px;background:var(--white);overflow:hidden}
  .slide > svg.art{position:absolute;left:0;top:0;width:286px;height:179px}
  .abs{position:absolute}
  .brand{position:absolute;display:flex;align-items:center;gap:2px;font-weight:600;color:var(--navy);font-size:8px;line-height:1}
  .brand .dot{width:7px;height:7px;border-radius:50%;background:var(--navy)}
  .brand.light{color:var(--white)}
  .brand.light .dot{background:var(--white)}
  .brand.big{font-size:14px;gap:4px}
  .brand.big .dot{width:12px;height:12px}
  .title{font-family:"Montserrat",sans-serif;font-size:9.5px;font-weight:400;color:var(--navy)}
  .title b{font-weight:700}
  .copy{font-size:3.3px;line-height:1.4;color:var(--ink);text-align:justify}
  .center{text-align:center}
  .green{color:var(--green)}
  .navy{color:var(--navy)}
  .svc-name{font-size:6px;color:var(--navy)}
  .svc-sub{font-size:3.2px;color:var(--ink)}
</style>
</head>
<body>

<svg width="0" height="0" style="position:absolute" aria-hidden="true">
  <defs>
    <linearGradient id="photoTone" x1="0" y1="0" x2="1" y2="1">
      <stop offset="0" stop-color="#1b2a55"/>
      <stop offset="0.55" stop-color="#1f5a4e"/>
      <stop offset="1" stop-color="#5fae45"/>
    </linearGradient>
    <linearGradient id="photoToneDark" x1="0" y1="0" x2="1" y2="1">
      <stop offset="0" stop-color="#2f6f49"/>
      <stop offset="0.6" stop-color="#173048"/>
      <stop offset="1" stop-color="#14163f"/>
    </linearGradient>
    <linearGradient id="panelTone" x1="1" y1="0" x2="0" y2="1">
      <stop offset="0" stop-color="#6cc04a"/>
      <stop offset="0.35" stop-color="#24584a"/>
      <stop offset="0.75" stop-color="#172f4f"/>
      <stop offset="1" stop-color="#15164a"/>
    </linearGradient>
    <linearGradient id="officeTone" x1="0" y1="0" x2="1" y2="0">
      <stop offset="0" stop-color="#6d6d72"/>
      <stop offset="0.5" stop-color="#c9c6c2"/>
      <stop offset="1" stop-color="#9a9897"/>
    </linearGradient>
    <symbol id="user" viewBox="0 0 20 20">
      <circle cx="10" cy="6" r="3.6" fill="currentColor"/>
      <path d="M3.5 17 C3.5 12 6.5 10.5 10 10.5 C13.5 10.5 16.5 12 16.5 17 Z" fill="currentColor"/>
    </symbol>
    <symbol id="cornerBlob" viewBox="0 0 40 60">
      <path d="M0 0 C8 4 10 12 7 22 C4 34 8 48 22 55 C30 58 36 59 40 60 H0 Z" fill="#6cc04a"/>
    </symbol>
  </defs>
</svg>

<!-- Slide 1: cover -->
<section class="slide cover" style="left:79px;top:78px">
  <svg class="art" viewBox="0 0 286 179">
    <path role="img" aria-label="Photo of businessmen reviewing documents at a desk" d="M0 0 H178 C162 12 150 30 153 55 C156 80 136 100 138 125 C140 150 170 160 190 179 H0 Z" fill="url(#photoTone)"/>
    <path d="M161 25 C165 20 172 20 171 23 C169 28 162 30 161 25 Z" fill="#2f6f49"/>
    <path d="M148 140 C146 133 150 130 155 133 C158 138 155 146 150 145 Z" fill="#6cc04a"/>
  </svg>
  <div class="brand big" style="right:10px;top:12px"><span class="dot"></span>Veridane</div>
  <div class="abs" style="right:10px;top:66px;text-align:right;font-family:'Bebas Neue',sans-serif;font-size:25px;line-height:0.98">
    <div class="green">Presentation</div>
    <div class="navy">Title Goes Here</div>
  </div>
  <div class="abs" style="right:10px;top:118px;font-size:5px">Subtitle of Presentation Goes Here</div>
  <div class="abs" style="right:8px;top:162px;background:var(--navy);color:#fff;font-size:3.6px;padding:2px 4px;border-radius:4px">Friday, August, 2023</div>
</section>

<!-- Slide 2: about us with services -->
<section class="slide" style="left:405px;top:78px">
  <svg class="art" viewBox="0 0 286 179">
    <path d="M0 0 H266 A4 4 0 0 1 270 4 H0 Z" fill="var(--navy)"/>
    <use href="#cornerBlob" x="0" y="124" width="38" height="55"/>
    <circle cx="153" cy="47" r="7.5" fill="var(--navy)"/><use href="#user" x="148" y="42" width="10" height="10" color="#fff"/>
    <circle cx="153" cy="77" r="7.5" fill="var(--navy)"/><use href="#user" x="148" y="72" width="10" height="10" color="#fff"/>
    <circle cx="153" cy="106" r="7.5" fill="var(--navy)"/><use href="#user" x="148" y="101" width="10" height="10" color="#fff"/>
    <circle cx="153" cy="136" r="7.5" fill="var(--navy)"/><use href="#user" x="148" y="131" width="10" height="10" color="#fff"/>
  </svg>
  <div class="brand" style="right:8px;top:11px"><span class="dot"></span>Veridane</div>
  <div class="abs title" style="left:30px;top:33px">About <b>Us</b></div>
  <div class="abs copy" style="left:30px;top:49px;width:93px">Lorem ipsum dolor sit amet, consectetuer adipiscing elit, sed diam nonummy nibh euismod tincidunt ut laoreet dolore magna aliquam erat volutpat. Ut wisi enim ad minim veniam, quis nostrud exerci tation ullamcorper suscipit lobortis nisl ut aliquip ex ea commodo consequat. Duis autem vel eum iriure dolor in hendrerit in vulputate velit esse molestie consequat.</div>
  <div class="abs copy" style="left:30px;top:102px;width:93px">Lorem ipsum dolor sit amet, consectetuer adipiscing elit, sed diam nonummy nibh euismod tincidunt ut laoreet dolore magna aliquam erat volutpat. Ut wisi enim ad minim veniam, quis nostrud exerci tation ullamcorper suscipit lobortis nisl ut aliquip ex ea commodo consequat. Duis autem vel eum iriure dolor in hendrerit in vulputate velit esse molestie consequat.</div>
  <div class="abs" style="left:170px;top:40px"><div class="svc-name">Service Title Goes Here</div><div class="svc-sub">Vivamus eu dull ex. curobour dopibus</div></div>
  <div class="abs" style="left:170px;top:70px"><div class="svc-name">Service Title Goes Here</div><div class="svc-sub">Vivamus eu dull ex. curobour dopibus</div></div>
  <div class="abs" style="left:170px;top:99px"><div class="svc-name">Service Title Goes Here</div><div class="svc-sub">Vivamus eu dull ex. curobour dopibus</div></div>
  <div class="abs" style="left:170px;top:129px"><div class="svc-name">Service Title Goes Here</div><div class="svc-sub">Vivamus eu dull ex. curobour dopibus</div></div>
</section>

<!-- Slide 3: our service timeline -->
<section class="slide" style="left:79px;top:290px">
  <svg class="art" viewBox="0 0 286 179">
    <path d="M0 0 H266 A4 4 0 0 1 270 4 H0 Z" fill="var(--navy)"/>
    <use href="#cornerBlob" x="0" y="124" width="58" height="55"/>
    <line x1="21" y1="106" x2="265" y2="106" stroke="var(--green)" stroke-width="0.6"/>
    <g fill="#fff" stroke="var(--green)" stroke-width="0.8">
      <circle cx="41" cy="89" r="10"/><circle cx="92" cy="89" r="10"/><circle cx="144" cy="89" r="10"/><circle cx="195" cy="89" r="10"/><circle cx="247" cy="89" r="10"/>
    </g>
    <g stroke="var(--green)" stroke-width="0.6">
      <line x1="41" y1="99" x2="41" y2="106"/><line x1="92" y1="99" x2="92" y2="106"/><line x1="144" y1="99" x2="144" y2="106"/><line x1="195" y1="99" x2="195" y2="106"/><line x1="247" y1="99" x2="247" y2="106"/>
    </g>
    <g color="var(--navy)">
      <use href="#user" x="35" y="83" width="12" height="12"/><use href="#user" x="86" y="83" width="12" height="12"/><use href="#user" x="138" y="83" width="12" height="12"/><use href="#user" x="189" y="83" width="12" height="12"/><use href="#user" x="241" y="83" width="12" height="12"/>
    </g>
  </svg>
  <div class="brand" style="right:8px;top:11px"><span class="dot"></span>Veridane</div>
  <div class="abs title" style="left:21px;top:27px">Our <b>Service</b></div>
  <div class="abs copy" style="left:20px;top:48px;width:244px;text-align:left">Lorem ipsum dolor sit amet, consectetuer adipiscing elit, sed diam nonummy nibh euismod tincidunt ut laoreet dolore magna aliquam erat volutpat. Ut wisi enim ad minim veniam, quis nostrud exerci tation ullamcorper suscipit lobortis nisl ut aliquip ex ea commodo consequat. Duis autem vel eum iriure dolor in hendrerit in vulputate velit esse molestie consequat.</div>
  <div class="abs center" style="left:16px;top:110px;width:50px"><div class="green" style="font-size:5.5px">Service Title</div><div style="font-size:4.5px;font-weight:500">Goes Here</div><div style="font-size:3.2px;margin-top:5px">Vivamus eu dull ex. curobour dopibus</div></div>
  <div class="abs center" style="left:67px;top:110px;width:50px"><div class="green" style="font-size:5.5px">Service Title</div><div style="font-size:4.5px;font-weight:500">Goes Here</div><div style="font-size:3.2px;margin-top:5px">Vivamus eu dull ex. curobour dopibus</div></div>
  <div class="abs center" style="left:119px;top:110px;width:50px"><div class="green" style="font-size:5.5px">Service Title</div><div style="font-size:4.5px;font-weight:500">Goes Here</div><div style="font-size:3.2px;margin-top:5px">Vivamus eu dull ex. curobour dopibus</div></div>
  <div class="abs center" style="left:170px;top:110px;width:50px"><div class="green" style="font-size:5.5px">Service Title</div><div style="font-size:4.5px;font-weight:500">Goes Here</div><div style="font-size:3.2px;margin-top:5px">Vivamus eu dull ex. curobour dopibus</div></div>
  <div class="abs center" style="left:222px;top:110px;width:50px"><div class="green" style="font-size:5.5px">Service Title</div><div style="font-size:4.5px;font-weight:500">Goes Here</div><div style="font-size:3.2px;margin-top:5px">Vivamus eu dull ex. curobour dopibus</div></div>
</section>

<!-- Slide 4: about us with photo -->
<section class="slide" style="left:405px;top:290px">
  <svg class="art" viewBox="0 0 286 179">
    <path d="M0 0 H266 A4 4 0 0 1 270 4 H0 Z" fill="var(--navy)"/>
    <use href="#cornerBlob" x="0" y="128" width="30" height="51"/>
    <path role="img" aria-label="Photo of two colleagues discussing work at a table" d="M208 179 L286 179 L286 108 L252 72 C225 44 168 46 153 86 C145 110 158 130 175 150 Z" fill="url(#photoToneDark)"/>
  </svg>
  <div class="brand" style="right:8px;top:11px"><span class="dot"></span>Veridane</div>
  <div class="abs title" style="left:17px;top:51px">About <b>Us</b></div>
  <div class="abs copy" style="left:17px;top:74px;width:124px">Lorem ipsum dolor sit amet, consectetuer adipiscing elit, sed diam nonummy nibh euismod tincidunt ut laoreet dolore magna aliquam erat volutpat. Ut wisi enim ad minim veniam, quis nostrud exerci tation ullamcorper suscipit lobortis nisl ut aliquip ex ea commodo consequat. Duis autem vel eum iriure dolor in hendrerit in vulputate velit esse molestie consequat.</div>
  <div class="abs copy" style="left:17px;top:110px;width:124px">Lorem ipsum dolor sit amet, consectetuer adipiscing elit, sed diam nonummy nibh euismod tincidunt ut laoreet dolore magna aliquam erat volutpat. Ut wisi enim ad minim veniam, quis nostrud exerci tation ullamcorper suscipit lobortis nisl ut aliquip ex ea commodo consequat. Duis autem vel eum iriure dolor in hendrerit in vulputate velit esse molestie consequat.</div>
</section>

<!-- Slide 5: photo band with three headings -->
<section class="slide" style="left:79px;top:501px">
  <svg class="art" viewBox="0 0 286 179">
    <path d="M0 0 H266 A4 4 0 0 1 270 4 H0 Z" fill="var(--navy)"/>
    <use href="#cornerBlob" x="0" y="128" width="42" height="51"/>
    <rect role="img" aria-label="Photo of three women working on laptops in an office" x="10" y="28" width="267" height="51" fill="url(#officeTone)"/>
    <g fill="var(--green)" stroke="#fff" stroke-width="1">
      <circle cx="127" cy="79" r="5.5"/><circle cx="187" cy="79" r="5.5"/><circle cx="247" cy="79" r="5.5"/>
    </g>
    <g color="#fff"><use href="#user" x="123.5" y="75.5" width="7" height="7"/><use href="#user" x="183.5" y="75.5" width="7" height="7"/><use href="#user" x="243.5" y="75.5" width="7" height="7"/></g>
  </svg>
  <div class="brand" style="right:8px;top:11px"><span class="dot"></span>Veridane</div>
  <div class="abs" style="left:10px;top:86px;font-size:9.5px;line-height:1.05"><div class="green">Heading</div><div class="navy">Goes Here</div></div>
  <div class="abs copy" style="left:10px;top:118px;width:74px;text-align:left">Lorem ipsum dolor sit amet, consectetuer adipiscing elit, sed diam nonummy nibh euismod tincidunt ut laoreet dolore magna aliquam erat volutpat. Ut wisi enim ad minim veniam, quis nostrud exerci tation</div>
  <div class="abs center" style="left:104px;top:92px;width:46px"><div class="green" style="font-size:6.5px">Heading</div><div class="copy center" style="margin-top:3px">Lorem ipsum dolor sit amet, consectetuer adipiscing elit, sed diam nonummy nibh euismod tincidunt ut laoreet dolore magna aliquam erat volutpat. Ut wisi enim ad minim veniam, quis nostrud exerci tation</div></div>
  <div class="abs center" style="left:164px;top:92px;width:46px"><div class="green" style="font-size:6.5px">Heading</div><div class="copy center" style="margin-top:3px">Lorem ipsum dolor sit amet, consectetuer adipiscing elit, sed diam nonummy nibh euismod tincidunt ut laoreet dolore magna aliquam erat volutpat. Ut wisi enim ad minim veniam, quis nostrud exerci tation</div></div>
  <div class="abs center" style="left:224px;top:92px;width:46px"><div class="green" style="font-size:6.5px">Heading</div><div class="copy center" style="margin-top:3px">Lorem ipsum dolor sit amet, consectetuer adipiscing elit, sed diam nonummy nibh euismod tincidunt ut laoreet dolore magna aliquam erat volutpat. Ut wisi enim ad minim veniam, quis nostrud exerci tation</div></div>
</section>

<!-- Slide 6: four pill cards -->
<section class="slide" style="left:405px;top:501px">
  <svg class="art" viewBox="0 0 286 179">
    <path d="M0 0 H266 A4 4 0 0 1 270 4 H0 Z" fill="var(--navy)"/>
    <use href="#cornerBlob" x="0" y="128" width="36" height="51"/>
    <g fill="var(--navy)">
      <rect x="23" y="61" width="51" height="95" rx="25.5"/><rect x="86" y="61" width="51" height="95" rx="25.5"/><rect x="149" y="61" width="51" height="95" rx="25.5"/><rect x="213" y="61" width="51" height="95" rx="25.5"/>
    </g>
    <g fill="var(--green)"><circle cx="48.5" cy="80" r="4.5"/><circle cx="111.5" cy="80" r="4.5"/><circle cx="174.5" cy="80" r="4.5"/><circle cx="238.5" cy="80" r="4.5"/></g>
    <g color="#fff"><use href="#user" x="45.5" y="77" width="6" height="6"/><use href="#user" x="108.5" y="77" width="6" height="6"/><use href="#user" x="171.5" y="77" width="6" height="6"/><use href="#user" x="235.5" y="77" width="6" height="6"/></g>
  </svg>
  <div class="brand" style="right:8px;top:11px"><span class="dot"></span>Veridane</div>
  <div class="abs" style="left:12px;top:23px;font-size:8.5px;color:var(--navy)"><b style="font-weight:600">Heading</b> Goes Here</div>
  <div class="abs copy" style="left:11px;top:39px;width:262px;text-align:left">Lorem ipsum dolor sit amet, consectetuer adipiscing elit, sed diam nonummy nibh euismod tincidunt ut laoreet dolore magna aliquam erat volutpat. Ut wisi enim ad minim veniam, quis nostrud exerci tation ullamcorper suscipit lobortis nisl ut aliquip ex ea commodo consequat. Duis autem vel eum iriure dolor in hendrerit in vulputate velit esse molestie consequat.</div>
  <div class="abs center" style="left:27px;top:89px;width:43px;color:#fff"><div style="font-size:6px">Heading</div><div style="font-size:3.1px;line-height:1.3;margin-top:3px">Lorem ipsum dolor sit amet, consectetuer adipiscing elit, sed diam nonummy nibh euismod tincidunt ut laoreet dolore magna aliquam erat volutpat. Ut wisi enim ad minim veniam, quis nostrud exerci tation</div></div>
  <div class="abs center" style="left:90px;top:89px;width:43px;color:#fff"><div style="font-size:6px">Heading</div><div style="font-size:3.1px;line-height:1.3;margin-top:3px">Lorem ipsum dolor sit amet, consectetuer adipiscing elit, sed diam nonummy nibh euismod tincidunt ut laoreet dolore magna aliquam erat volutpat. Ut wisi enim ad minim veniam, quis nostrud exerci tation</div></div>
  <div class="abs center" style="left:153px;top:89px;width:43px;color:#fff"><div style="font-size:6px">Heading</div><div style="font-size:3.1px;line-height:1.3;margin-top:3px">Lorem ipsum dolor sit amet, consectetuer adipiscing elit, sed diam nonummy nibh euismod tincidunt ut laoreet dolore magna aliquam erat volutpat. Ut wisi enim ad minim veniam, quis nostrud exerci tation</div></div>
  <div class="abs center" style="left:217px;top:89px;width:43px;color:#fff"><div style="font-size:6px">Heading</div><div style="font-size:3.1px;line-height:1.3;margin-top:3px">Lorem ipsum dolor sit amet, consectetuer adipiscing elit, sed diam nonummy nibh euismod tincidunt ut laoreet dolore magna aliquam erat volutpat. Ut wisi enim ad minim veniam, quis nostrud exerci tation</div></div>
</section>

<!-- Slide 7: text, chart and photo panel -->
<section class="slide" style="left:79px;top:713px">
  <svg class="art" viewBox="0 0 286 179">
    <use href="#cornerBlob" x="0" y="128" width="56" height="51"/>
    <path role="img" aria-label="Photo of business people shaking hands in silhouette" d="M286 0 H215 C209 0 208 12 200 12 H176 C168 12 166 22 166 30 C166 38 160 42 152 42 C144 42 144 52 152 52 H172 C178 52 178 62 172 62 H150 C142 62 142 72 150 72 H170 C176 72 176 82 170 82 H148 C140 82 140 92 148 92 H176 C182 92 182 102 176 102 H148 C140 102 140 112 148 112 H178 C184 112 184 122 178 122 H150 C142 122 142 132 150 132 H170 C176 132 176 142 170 142 H148 C140 142 140 152 148 152 H184 C190 152 190 162 184 162 H158 C150 162 150 172 158 172 H180 C184 172 184 179 188 179 H286 Z" fill="url(#panelTone)"/>
    <g stroke="#cfcfd6" stroke-width="0.25">
      <line x1="20" y1="108" x2="132" y2="108"/><line x1="20" y1="115.5" x2="132" y2="115.5"/><line x1="20" y1="123" x2="132" y2="123"/><line x1="20" y1="130.5" x2="132" y2="130.5"/><line x1="20" y1="138" x2="132" y2="138"/><line x1="20" y1="145.5" x2="132" y2="145.5"/><line x1="20" y1="153" x2="132" y2="153"/>
    </g>
    <g font-family="Montserrat,sans-serif" font-size="2.2" fill="#333">
      <text x="17" y="154">0</text><text x="17" y="146.5">1</text><text x="17" y="139">2</text><text x="17" y="131.5">3</text><text x="17" y="124">4</text><text x="17" y="116.5">5</text><text x="17" y="109">6</text>
      <text x="29" y="157.5">Category 1</text><text x="57" y="157.5">Category 2</text><text x="84" y="157.5">Category 3</text><text x="112" y="157.5">Category 4</text>
    </g>
    <g>
      <rect x="25" y="120.3" width="5.5" height="32.7" fill="var(--green)"/><rect x="32" y="135" width="5.5" height="18" fill="#9a9ba3"/><rect x="39" y="138" width="5.5" height="15" fill="var(--navy)"/>
      <rect x="53" y="134.3" width="5.5" height="18.7" fill="#9a9ba3"/><rect x="60" y="119.6" width="5.5" height="33.4" fill="var(--green)"/><rect x="67" y="138" width="5.5" height="15" fill="var(--navy)"/>
      <rect x="81" y="126.8" width="5.5" height="26.2" fill="var(--navy)"/><rect x="88" y="139.5" width="5.5" height="13.5" fill="#9a9ba3"/><rect x="95" y="130.5" width="5.5" height="22.5" fill="var(--green)"/>
      <rect x="108" y="119.6" width="5.5" height="33.4" fill="#9a9ba3"/><rect x="115" y="132" width="5.5" height="21" fill="var(--navy)"/><rect x="122" y="115.5" width="5.5" height="37.5" fill="var(--green)"/>
    </g>
  </svg>
  <div class="brand light" style="right:8px;top:11px"><span class="dot"></span>Veridane</div>
  <div class="abs copy" style="left:17px;top:30px;width:113px">Lorem ipsum dolor sit amet, consectetuer adipiscing elit, sed diam nonummy nibh euismod tincidunt ut laoreet dolore magna aliquam erat volutpat. Ut wisi enim ad minim veniam, quis nostrud exerci tation ullamcorper suscipit lobortis nisl ut aliquip ex ea commodo consequat. Duis autem vel eum iriure dolor in hendrerit in vulputate velit</div>
  <div class="abs copy" style="left:17px;top:66px;width:113px">Lorem ipsum dolor sit amet, consectetuer adipiscing elit, sed diam nonummy nibh euismod tincidunt ut laoreet dolore magna aliquam erat volutpat. Ut wisi enim ad minim veniam, quis nostrud exerci tation ullamcorper suscipit lobortis nisl ut aliquip ex ea commodo consequat. Duis autem vel eum iriure dolor in hendrerit in vulputate velit esse molestie consequat.</div>
</section>

<!-- Slide 8: our service with gauges -->
<section class="slide" style="left:405px;top:713px">
  <svg class="art" viewBox="0 0 286 179">
    <path d="M0 0 H266 A4 4 0 0 1 270 4 H0 Z" fill="var(--navy)"/>
    <use href="#cornerBlob" x="0" y="128" width="30" height="51"/>
    <path role="img" aria-label="Photo of a businessman seated at a desk in a modern office" d="M208 179 L286 179 L286 108 L252 72 C225 44 168 46 153 86 C145 110 158 130 175 150 Z" fill="url(#photoToneDark)"/>
    <g fill="#fff" stroke="#9a9ba3" stroke-width="0.5"><circle cx="25" cy="48" r="6.5"/><circle cx="25" cy="73" r="6.5"/></g>
    <g color="var(--green)"><use href="#user" x="20.5" y="43.5" width="9" height="9"/><use href="#user" x="20.5" y="68.5" width="9" height="9"/></g>
    <g fill="none" stroke-width="1.6">
      <circle cx="46" cy="131" r="13" stroke="#e8e8ee"/>
      <circle cx="46" cy="131" r="13" stroke="var(--green)" stroke-dasharray="61.3 20.4" transform="rotate(-90 46 131)"/>
      <circle cx="94" cy="131" r="13" stroke="#e8e8ee"/>
      <circle cx="94" cy="131" r="13" stroke="var(--green)" stroke-dasharray="61.3 20.4" transform="rotate(-90 94 131)"/>
    </g>
    <g stroke="var(--navy)" stroke-width="1.1" fill="none">
      <path d="M46 118 A13 13 0 0 0 33 131"/><path d="M94 118 A13 13 0 0 0 81 131"/>
    </g>
  </svg>
  <div class="brand" style="right:8px;top:11px"><span class="dot"></span>Veridane</div>
  <div class="abs title" style="left:17px;top:18px">Our <b>Service</b></div>
  <div class="abs" style="left:38px;top:41px"><div class="green" style="font-size:6px">Service Title Goes Here</div><div class="svc-sub">Vivamus eu dull ex. curobour dopibus</div></div>
  <div class="abs" style="left:38px;top:66px"><div class="green" style="font-size:6px">Service Title Goes Here</div><div class="svc-sub">Vivamus eu dull ex. curobour dopibus</div></div>
  <div class="abs copy" style="left:17px;top:85px;width:117px">Lorem ipsum dolor sit amet, consectetuer adipiscing elit, sed diam nonummy nibh euismod tincidunt ut laoreet dolore magna aliquam erat volutpat. Ut wisi enim ad minim veniam, quis nostrud exerci tation ullamcorper suscipit lobortis nisl ut aliquip ex ea commodo consequat. Duis autem vel eum iriure dolor in hendrerit in vulputate velit esse molestie consequat.</div>
  <div class="abs center green" style="left:33px;top:127px;width:26px;font-size:6px">75%</div>
  <div class="abs center green" style="left:81px;top:127px;width:26px;font-size:6px">75%</div>
  <div class="abs center" style="left:26px;top:148px;width:40px"><div style="font-size:4.4px;font-weight:600;color:var(--navy)">Heading</div><div style="font-size:3px">adipiscing elit. Vivamus eu dui ex. Cutabitur</div></div>
  <div class="abs center" style="left:74px;top:148px;width:40px"><div style="font-size:4.4px;font-weight:600;color:var(--navy)">Heading</div><div style="font-size:3px">adipiscing elit. Vivamus eu dui ex. Cutabitur</div></div>
</section>

<!-- Slide 9: closing -->
<section class="slide closing" style="left:232px;top:925px">
  <svg class="art" viewBox="0 0 286 179">
    <path role="img" aria-label="Photo looking up at glass office towers" d="M0 0 H178 C162 12 150 30 153 55 C156 80 136 100 138 125 C140 150 170 160 190 179 H0 Z" fill="url(#photoToneDark)"/>
    <path d="M161 25 C165 20 172 20 171 23 C169 28 162 30 161 25 Z" fill="#1f4a3a"/>
    <path d="M148 140 C146 133 150 130 155 133 C158 138 155 146 150 145 Z" fill="#1f4a3a"/>
  </svg>
  <div class="brand big" style="right:13px;top:12px"><span class="dot"></span>Veridane</div>
  <div class="abs" style="right:14px;top:52px;text-align:right;font-family:'Bebas Neue',sans-serif;font-size:44px;line-height:0.9">
    <div style="color:var(--ghost)">Thank</div>
    <div style="color:var(--ghost-green)">You!</div>
  </div>
  <div class="abs" style="right:14px;top:158px;text-align:right;font-size:7.5px;font-weight:700;line-height:1;color:var(--navy)">PRESENTATION<br>TITLE GOES HERE</div>
</section>

</body>
</html>
```